Vocational Mentor needs an impressive business card

1. I need a business card (or maybe three with identic look) to promote me and my three business titles/services:
- Vocational Mentor. I help people find their vocation and live happily from it. I use my 20 years of experience in business, management and psychology to help them identify the most efficient ways to make a living doing what they are passionate about.
- Business Angel. I help founders start a succesful business with minimum risks and costs. I use my 20 years of experience in sales, management and entrepreneurship to help them identify the most efficient ways, in terms of time and cost, to validate their business idea.
- Learning Designer. I design unique learning programs that produce long-term cognitive and behavioural changes to people and organisations. I use my 20 years of experience in learning, teaching and change management to create minimalist experiences and processes that allow them to change efficiently in their pursued direction.

2. I would like a two-sided business card, on the front with my name, contact details and titles, on the back the explanation of the services.
Updates

Hi all,

I updated my brief, included contacts info and give feedback on all designs I got. I am new on this platform so please tell me if you need anything else or if I don't use corectly the platform forms.

Kind regards,
Tudor

Hi all,

I shortened the services description by deleting the phrase "I call..."

Kind regards,
Tudor

Target Market(s)

Freelancers, startups, people and organization willing to invest in change through ultimate learning experiences

Industry/Entity Type

Business

Font styles to use
Serif

Requirements
Must have
• Front side: full name, titles, web site, email, phone like below:
Tudor Vasilache
Vocational Mentor, Business Angel, Learning Designer
info@tudorvasilache.example
www.tudorvasilache.example
+40-745-TUDORV
Nice to have
• Back side: the description of the services I provide as in the task description.
1/3: it would be nice if I can jam all three titles on the front side but then I need a solution to jam all three services on the back side.

```html
<!DOCTYPE html>
<html lang="en">
<head>
<meta charset="utf-8">
<title>Tudor Vasilache – Business Card</title>
<link rel="stylesheet" href="https://fonts.googleapis.com/css2?family=Source+Serif+4:opsz,wght@8..60,400;8..60,700&display=swap">
<style>
  :root {
    --brand: #3a3387;
    --paper: #ffffff;
    --page: #ffffff;
    --ink: #2b2b2b;
    --on-brand: #ffffff;
    --art-light: #e6e8f4;
    --art-mid: #9fa3cf;
    --art-gold: #c9a93a;
  }
  * { box-sizing: border-box; margin: 0; padding: 0; }
  html, body {
    width: 1026px; height: 1200px; overflow: hidden;
    background: var(--page);
    font-family: "Source Serif 4", Georgia, serif;
  }
  .canvas { position: relative; width: 1026px; height: 1200px; }

  .card {
    position: absolute; left: 134px; width: 748px;
    background: var(--paper);
    box-shadow: 0 0 14px rgba(0,0,0,0.12);
    overflow: hidden;
  }
  .card--front { top: 99px; height: 430px; }
  .card--back { top: 643px; height: 428px; }

  /* front */
  .front-band {
    position: absolute; left: 0; top: 0; width: 100%; height: 227px;
    background: var(--brand);
  }
  .wordmark {
    position: absolute; color: var(--on-brand);
    font-weight: 700; line-height: 1.05; letter-spacing: 0.5px;
  }
  .front-band .wordmark { left: 49px; top: 62px; font-size: 21px; }
  .identity { position: absolute; left: 185px; top: 46px; color: var(--on-brand); }
  .identity__name { font-size: 25px; font-weight: 700; line-height: 30px; }
  .contact {
    display: flex; align-items: center; gap: 12px;
    font-size: 20px; line-height: 24px; margin-top: 13px;
  }
  .contact svg { width: 19px; height: 19px; flex: none; }

  .titles {
    position: absolute; left: 160px; top: 243px;
    list-style: none; color: var(--brand);
  }
  .titles li {
    font-size: 31px; font-weight: 700; letter-spacing: 0.3px;
    height: 53px; display: flex; align-items: center;
  }
  .titles li::before {
    content: "•"; font-size: 20px; margin-right: 16px;
  }
  .front-art {
    position: absolute; left: 522px; top: 172px; width: 200px; height: 239px;
    background:
      radial-gradient(circle at 30% 20%, var(--art-gold) 0 18%, transparent 30%),
      radial-gradient(ellipse at 55% 60%, var(--art-mid) 0 35%, var(--art-light) 60%, var(--paper) 80%);
  }

  /* back */
  .services { position: absolute; left: 45px; top: 20px; width: 670px; }
  .service { margin-bottom: 8px; }
  .service__title {
    color: var(--brand); font-size: 24px; line-height: 30px; font-weight: 700; letter-spacing: 0.3px;
  }
  .service__title::before { content: "• "; }
  .service__text {
    margin-left: 61px; width: 609px;
    color: var(--ink); font-size: 15px; line-height: 19px;
    text-align: justify;
  }
  .back-band {
    position: absolute; left: 0; bottom: 0; width: 100%; height: 14px;
    background: var(--brand);
  }
  .card--back .wordmark {
    color: var(--brand); left: 19px; top: 377px; font-size: 13px;
  }
</style>
</head>
<body>
<main class="canvas">

  <section class="card card--front" aria-label="Business card front">
    <div class="front-band">
      <div class="wordmark">Tudor<br>Vasilache</div>
      <div class="identity">
        <h1 class="identity__name">Tudor Vasilache</h1>
        <p class="contact">
          <svg viewBox="0 0 20 20" aria-hidden="true" fill="none" stroke="#fff" stroke-width="1.4">
            <rect x="2" y="4.5" width="16" height="11" rx="1"/><polyline points="2.5,5 10,11 17.5,5"/>
          </svg>
          info@tudorvasilache.example
        </p>
        <p class="contact">
          <svg viewBox="0 0 20 20" aria-hidden="true" fill="none" stroke="#fff" stroke-width="1.2">
            <circle cx="10" cy="10" r="8"/><ellipse cx="10" cy="10" rx="3.5" ry="8"/>
            <line x1="2" y1="10" x2="18" y2="10"/><line x1="3.5" y1="6" x2="16.5" y2="6"/><line x1="3.5" y1="14" x2="16.5" y2="14"/>
          </svg>
          www.tudorvasilache.example
        </p>
        <p class="contact">
          <svg viewBox="0 0 20 20" aria-hidden="true" fill="none" stroke="#fff" stroke-width="1.4">
            <rect x="5" y="2" width="10" height="16" rx="1.5"/><line x1="5" y1="14" x2="15" y2="14"/>
          </svg>
          +40-745-TUDORV
        </p>
      </div>
    </div>
    <ul class="titles">
      <li>Vocational Mentor</li>
      <li>Business Angel</li>
      <li>Learning Designer</li>
    </ul>
    <div class="front-art" role="img" aria-label="Illustration of a golden key turning in a blue puzzle piece"></div>
  </section>

  <section class="card card--back" aria-label="Business card back">
    <div class="services">
      <article class="service">
        <h2 class="service__title">Vocational Mentor</h2>
        <p class="service__text">I help people to find their vocation and live happily from it. I use my 20 years of experience in business, management and psychology to help them identify the most efficient ways to make a living doing what they are passionate about. I call this service vocational mentoring.</p>
      </article>
      <article class="service">
        <h2 class="service__title">Business Angel</h2>
        <p class="service__text">I help founders to start a succesful business with minimum risks and costs. I use my 20 years of experience in sales, management and entrepreneurship to help them identify the most efficient ways, in terms of time and cost, to validate their business idea. I call this service lean-startup mentoring.</p>
      </article>
      <article class="service">
        <h2 class="service__title">Learning Designer</h2>
        <p class="service__text">I design unique learning programs that produce long-term cognitive and behavioural changes to people and organisations. I use my 20 years of experience in learning, teaching and change management to create minimalist experiences and processes that allows them to change efficiently in their pursued direction. I call this service ultimate learning design.</p>
      </article>
    </div>
    <div class="wordmark">Tudor<br>Vasilache</div>
    <div class="back-band"></div>
  </section>

</main>
</body>
</html>
```